Tidewell Marketing company is looking for a web page design

Your projects should contain:

1. Header: Logo provided by us.
2. Top nav bar: offer, about us, experience, contact.
3. “Choose language” button.
4. Main section: panoramic picture (static, professional, modern).
5. Below section: 3 blocks (image+title+description), which represent our 3 main activities (titles):
• Market Research,
• Marketing Plans,
• Marketing Project.
6. ‘Contact us’ form – Message (text: “Write your message and give us details about your company and activities”), Email, SEND).
7. Page footer: (4 section: Contact, Social Media, Blog, Partners).
Updates

Hello!

I uploaded new file 'general_look', which is our idea how the page should generally look like.

BUT! it doesn't mean that your projects should look exactly like this project e.g.:
* titles Market Research, Marketing Plans, Marketing Project can be above these: Image 1,2,3.
* everything doesn't have to be in square and rectangle shape. You can try to manipulate with blocks and can add elipse elemnts or something similar.

We will appreciate your innovative ideas. Just wanted to give you general plan of the site and ilustrate all elements that we require.

Best Regards,
Benedek

IMPORTENT

Please remember that the main picture should be panoramic. Please do not close it in frame.

Target Market(s)

Small and middle sized companies, which would like to export their goods and services abroad and are interested in raising funds from Northgate Trade Council to expand their activities. These are rather industrial companies with low level of innovativeness. Our mission is to build image of the client’s company and increase awareness of their products to improve their competitiveness and innovativeness.

Industry/Entity Type

It Company

Requirements
Must have
• 1. Create designs of main page and subpage.
2. Subpage: Logo, Header, language button, place for article, navigation menu on the right side - below it “contact us” button , footer on the bottom. (In this section we are looking mainly for the design of the header and navigation menu).
3. The whole design should be a series of horizontal blocks.
4. Your projects should be associated with features such as: Reliability, Security, Professionalism, Openness, Uniqueness.
5. The design should be simple, fresh, readable, easy to use and should create a feeling of high quality services.
6. Possibility to change the panoramic picture (separate layer in a graphic file).
7. All pictures and blocks should be static, no movements.
8. Style of the page should be compliant with the logo design, font: Swiss.
9. Designs that we like: http://www.fernvale-studio.pl/, http://www.plumquarry.com/.
Should not have
• There shouldn’t be any distractions and not matching parts (whole design should be compact and easy to interpret and remember).

```html
<!DOCTYPE html>
<html lang="en">
<head>
<meta charset="utf-8">
<title>Tidewell Marketing</title>
<link rel="stylesheet" href="https://fonts.googleapis.com/css2?family=Open+Sans:wght@300;400;600&display=swap">
<style>
:root{
  --bg-deep:#17589c;
  --bg-mid:#2a80c6;
  --bg-light:#3a95d6;
  --footer:#0a3760;
  --footer-text:#8fb3d3;
  --footer-head:#e6f1fb;
  --link:#4fb3ff;
  --btn-top:#64b6ea;
  --btn-bottom:#2a7dc2;
  --panel:#ffffff;
  --body-text:#333a40;
  --white:#ffffff;
  --frame:#8cc3ea;
}
*{margin:0;padding:0;box-sizing:border-box}
html,body{width:1200px;height:2188px;overflow:hidden}
body{
  position:relative;
  font-family:"Open Sans",Verdana,sans-serif;
  background:
    radial-gradient(ellipse 900px 700px at 600px 700px,var(--bg-light),transparent 70%),
    linear-gradient(180deg,var(--bg-deep) 0,var(--bg-mid) 420px,var(--bg-mid) 1815px);
}
.abs{position:absolute}
.btn{
  position:absolute;display:flex;align-items:center;justify-content:center;
  color:var(--white);border-radius:5px;
  background:linear-gradient(180deg,var(--btn-top),var(--btn-bottom));
  box-shadow:0 3px 5px rgba(0,30,70,.45);
}
/* header */
.brand{left:131px;top:70px;display:flex;align-items:center;gap:16px}
.brand-dot{width:78px;height:78px;border-radius:50%;background:#0f4f8f}
.brand-name{font-size:50px;font-weight:600;color:#0d3f72;letter-spacing:-1px;line-height:1}
.brand-tag{left:226px;top:138px;font-size:20px;color:#0d3f72}
.lang{left:837px;top:109px;width:255px;height:57px;font-size:22px;justify-content:flex-start;padding-left:20px}
.lang svg{position:absolute;right:20px;top:22px}
.nav{left:108px;top:190px;width:985px;height:71px;display:flex;border-radius:5px;overflow:hidden;
  background:linear-gradient(180deg,var(--btn-top),var(--btn-bottom));box-shadow:0 4px 7px rgba(0,30,70,.45)}
.nav a{display:flex;align-items:center;justify-content:center;color:var(--white);font-size:23px;text-decoration:none;border-right:1px solid rgba(10,60,110,.35)}
.nav a:last-child{border-right:0}
.nav .active{background:linear-gradient(180deg,#7cc4ee,#4c9fd8);color:#0d3f72}
/* hero */
.hero-art{left:180px;top:290px;width:914px;height:458px;
  background:radial-gradient(ellipse 360px 180px at 260px 150px,rgba(14,70,130,.55),transparent 75%),
             radial-gradient(ellipse 170px 240px at 790px 210px,rgba(5,20,40,.55),transparent 75%)}
.hero-title{left:146px;top:552px;color:var(--white);font-weight:400;line-height:1.2}
.hero-title b{display:block;font-weight:400;font-size:48px}
.hero-title span{display:block;font-size:35px}
/* services */
.panel{left:108px;top:748px;width:988px;height:729px;background:var(--panel);border-radius:4px;box-shadow:0 6px 16px rgba(0,30,70,.35)}
.service{position:absolute;top:771px;width:299px}
.service-title{position:relative;height:80px;font-size:27px;box-shadow:0 3px 5px rgba(0,30,70,.35)}
.service-photo{margin-top:19px;height:206px;border:4px solid var(--frame);border-radius:8px;background:linear-gradient(160deg,#dfe8ef,#9fb3c4)}
.service-text{margin:20px 0 0 4px;width:285px;font-size:20.5px;line-height:29.5px;color:var(--body-text);text-align:justify}
.more{width:80px;height:46px;font-size:19px}
/* contact */
.contact-head{left:119px;top:1508px;font-size:27px;color:var(--white)}
.field{position:absolute;background:var(--white);border:2px solid #c7dced;border-radius:4px;color:var(--body-text);font-size:21px;padding:0 14px;display:flex;align-items:center}
.message{left:109px;top:1556px;width:489px;height:208px;align-items:flex-start;padding-top:12px;line-height:29px}
.clear,.send{top:1709px;width:219px;height:57px;font-size:25px}
/* footer */
.footer{left:0;top:1815px;width:1200px;height:373px;background:var(--footer)}
.col{position:absolute;top:1855px;font-size:19.5px;line-height:28px;color:var(--footer-text)}
.col h3{font-weight:400;font-size:27px;color:var(--footer-head);margin-bottom:8px}
.divider{position:absolute;top:1862px;height:236px;border-left:2px dashed #1f5f98}
.link{color:var(--link)}
.social{display:flex;align-items:center;gap:28px;height:40px;margin-left:30px}
.social i{width:30px;height:30px;border-radius:4px;background:#3a6f9f;display:block}
.foot-more{width:77px;height:40px;font-size:19px;margin-top:8px;position:relative}
.copyright{left:0;width:1230px;top:2133px;text-align:center;font-size:17px;font-style:italic;color:#3f8fd0}
</style>
</head>
<body>

<header>
  <div class="abs brand"><span class="brand-dot"></span><span class="brand-name">Tidewell Marketing</span></div>
  <div class="abs brand-tag">your passport to foreign markets</div>
  <div class="btn lang">Choose Language
    <svg width="22" height="14" viewBox="0 0 22 14"><path d="M0 0h22L11 14z" fill="#1d5f9e"/></svg>
  </div>
  <nav class="abs nav">
    <a class="active" style="width:148px">Home</a>
    <a style="width:188px">We Offer</a>
    <a style="width:206px">About us</a>
    <a style="width:232px">Experience</a>
    <a style="width:211px">Contact Us</a>
  </nav>
</header>

<section>
  <div class="abs hero-art" role="img" aria-label="Panoramic world map with three business people in silhouette"></div>
  <h1 class="abs hero-title"><b>Tidewell Marketing</b><span>is more than just a name.</span></h1>
</section>

<section>
  <div class="abs panel"></div>

  <article class="service" style="left:128px">
    <div class="btn service-title">Market Research</div>
    <div class="service-photo" role="img" aria-label="Photo of a businessman working at a laptop"></div>
    <p class="service-text">Small and middle sized companies, which would like to export their goods and services abroad and are interested in raising funds from Northgate Trade Council. Small and middle sized companies, which would like to export their goods and services abroad.</p>
    <div class="btn more" style="left:3px;top:639px">More</div>
  </article>

  <article class="service" style="left:452px">
    <div class="btn service-title">Marketing Plans</div>
    <div class="service-photo" role="img" aria-label="Photo of folded hands of a man in a suit"></div>
    <p class="service-text">Small and middle sized companies, which would like to export their goods and services abroad and are interested in raising funds from Northgate Trade Council. Small and middle sized companies, which would like to export their goods and services abroad.</p>
    <div class="btn more" style="left:6px;top:639px">More</div>
  </article>

  <article class="service" style="left:775px">
    <div class="btn service-title">Marketing Project</div>
    <div class="service-photo" role="img" aria-label="Photo of a business handshake"></div>
    <p class="service-text">Small and middle sized companies, which would like to export their goods and services abroad and are interested in raising funds from Northgate Trade Council. Small and middle sized companies, which would like to export their goods and services abroad.</p>
    <div class="btn more" style="left:7px;top:639px">More</div>
  </article>
</section>

<section>
  <h2 class="abs contact-head" style="font-weight:400">Contact Us</h2>
  <div class="field message">Write your message and give us details about your company and activities</div>
  <div class="field" style="left:626px;top:1560px;width:465px;height:57px">Your Name</div>
  <div class="field" style="left:626px;top:1632px;width:465px;height:57px">Email Id</div>
  <div class="btn clear" style="left:626px">Clear</div>
  <div class="btn send" style="left:872px">Send</div>
</section>

<footer>
  <div class="abs footer"></div>
  <div class="divider" style="left:350px"></div>
  <div class="divider" style="left:604px"></div>
  <div class="divider" style="left:852px"></div>

  <div class="col" style="left:109px">
    <h3>Contacts</h3>
    18/4b, Harbour Lane,<br>Dunmore, OR<br>Email : hello@tidewell.example<br>Phone : 00-0417-3382/<br>&nbsp;&nbsp;&nbsp;&nbsp;&nbsp;&nbsp;&nbsp;&nbsp;&nbsp;&nbsp;&nbsp;&nbsp;&nbsp;0417-3390<br>Fax : 800-3108-6624/<br>&nbsp;&nbsp;&nbsp;&nbsp;&nbsp;&nbsp;&nbsp;&nbsp;&nbsp;&nbsp;3108-6631
  </div>

  <div class="col" style="left:365px">
    <h3>Social Media</h3>
    Follow Us :
    <div class="social"><i></i>Circlebook</div>
    <div class="social"><i></i>Pinwall</div>
    <div class="social"><i></i>Linkhall</div>
    <div class="social"><i></i>Orbitly</div>
  </div>

  <div class="col" style="left:624px">
    <h3>Blog</h3>
    <span class="link">Blog Title goes here</span><br>Dt: 21-Aug-2012<br>Description goes here.<br>Put something about<br>your topic.
    <div class="btn foot-more">More</div>
  </div>

  <div class="col" style="left:872px">
    <h3>Pertners</h3>
    We are joints hand with<br>renouned co. e.g.;<br><span class="link">Alder Corporation</span><br><span class="link">Yarrow Corporation</span><br><span class="link">Brightmill Ltd.</span>
    <div class="btn foot-more">More</div>
  </div>

  <p class="abs copyright">Copyright @ 2012, TidewellMarketing</p>
</footer>

</body>
</html>
```